Rudy Fenwick - Free Personalised Health Consultation - "One size does not fit all"

This flyer will be left on tables/seats at speaking events and seminars and used to attain leads.

Top half will have "SMS me for a FREE Personalised Health Consultation" and my picture (see www.rudyfenwick.example and pick most engaging photo) and underneath my contact details. It must have lines with "Notes:" halfway down so people can take notes at the seminar and lines on the back with my contact details again and "Notes: with lines.

I am having a business card also being designed by Artshelf for same and would like the flyer and business card to carry a similar feel/look for consistency.

Below is the brief for the business card being designed:
Business Card for www.rudyfenwick.example site. It is a trust site and I use it for 1:1 relatable connections. It is the one I use for building intimate 1:1 trust building and Exec Coaching Services and programs for high wealth individuals and corporates. I also have a commercial programmatic site of my personal health products and services and programs for main stream one to many. www.quietbirchliving.example that can also provoke thought for the www.rudyfenwick.example business card. (mind you will get a separate business card for that site, but want to provide context). It has a logo which you may want to draw from in designing the rudyfenwick business card which is personal and is about building my brand. There is also a rudyfenwick personal FB page and rudyfenwick business FB page. I am a Certified Talent Compass 3.1 Coach with Harlow and you can get a corporate brief of me on there to give you more context https://www.harlowtalenthub.example/coach/en-us/directory?search=rudy

Target Market(s)

Exec, IT, Health conscious. Corporates wanting to run Health and Wellness programs. Those wanting to go from good to great. Millennials to Middleaged.

Industry/Entity Type

Health And Wellness

Font styles to use
Sans Serif
Other font styles liked:
• Arial and Calibri ok too

Colors

Designer to choose colors to be used in the design.

Requirements
Must have
• Picture of me - use best from www.rudyfenwick.example or can send one you choose.
• Contact details like my buisness card being designed by you guys in separate project.
• Name: Rudy Fenwick
• email: rudy@rudyfenwick.,example
• Phone: Australia +61 400 000 000 Singapore: +65 9000 0000
Nice to have
• Open to ideas

```html
<!DOCTYPE html>
<html lang="en">
<head>
<meta charset="utf-8">
<title>Rudy Fenwick – Health Consultation Flyer</title>
<link href="https://fonts.googleapis.com/css2?family=Montserrat:wght@500;600;800&family=Arimo:wght@400&family=Nothing+You+Could+Do&display=swap" rel="stylesheet">
<style>
  :root {
    --stage: #000000;
    --paper: #ffffff;
    --brand-blue: #00a3e4;
    --brand-blue-deep: #0b93d1;
    --band-grey: #ececec;
    --band-grey-deep: #dcdddf;
    --disc-grey: #e8e8e8;
    --rule: #c9c9c9;
    --ink: #1a1a1a;
    --ink-soft: #4a4a4a;
    --footer-black: #0c0c0c;
  }
  * { margin: 0; padding: 0; box-sizing: border-box; }
  html, body { width: 1200px; height: 835px; overflow: hidden; background: var(--stage); }
  .canvas { position: relative; width: 1200px; height: 835px; background: var(--stage); }

  .page { position: absolute; top: 77px; width: 483px; height: 682px; background: var(--paper); overflow: hidden; }
  .page--front { left: 88px; }
  .page--back { left: 629px; }
  .page__art { position: absolute; inset: 0; width: 100%; height: 100%; }

  .headline { position: absolute; left: 32px; top: 76px; color: var(--paper);
    font-family: "Montserrat", sans-serif; font-weight: 800; text-transform: uppercase; }
  .headline__lead { display: block; font-size: 31px; line-height: 38px; letter-spacing: 0.5px; }
  .headline__line { display: block; font-size: 20.5px; line-height: 35.6px; letter-spacing: 0.4px; }

  .contact-list { position: absolute; left: 32px; top: 373px; list-style: none;
    font-family: "Montserrat", sans-serif; font-weight: 500; font-size: 8.6px; color: var(--ink-soft); }
  .contact-list li { display: flex; align-items: center; height: 18.3px; }
  .contact-list .icon { width: 14px; display: inline-flex; }
  .contact-list .icon svg { width: 8px; height: 8px; fill: var(--ink-soft); }

  .signature { position: absolute; font-family: "Nothing You Could Do", cursive; color: var(--ink); white-space: nowrap; }
  .signature--front { left: 260px; top: 386px; font-size: 25px; letter-spacing: 1px; }
  .signature--back { left: 357px; top: 620px; font-size: 16px; letter-spacing: 0.5px; }
  .signature--faint { left: 10px; top: 578px; font-size: 64px; color: #000; opacity: 0.06; letter-spacing: 4px; }

  .footer-contacts { position: absolute; top: 624px; left: 14px; display: flex;
    font-family: "Arimo", Arial, sans-serif; font-size: 9.4px; color: var(--paper); }
  .footer-contacts__col { list-style: none; }
  .footer-contacts__col li { display: flex; align-items: center; height: 16.5px; }
  .footer-contacts__col--phone { width: 153px; padding-left: 0; }
  .footer-contacts__col--web { padding-left: 10px; }
  .footer-contacts .icon { width: 15px; display: inline-flex; justify-content: center; }
  .footer-contacts .icon svg { width: 8px; height: 8px; fill: var(--paper); }
  .footer-contacts .gap { display: inline-block; width: 5px; }
</style>
</head>
<body>
<div class="canvas">

  <!-- Front page -->
  <section class="page page--front">
    <svg class="page__art" viewBox="0 0 596 842" preserveAspectRatio="none">
      <defs>
        <linearGradient id="portraitTone" x1="0" y1="0" x2="0" y2="1">
          <stop offset="0" stop-color="#9a9a9a"/>
          <stop offset="0.45" stop-color="#2a2a2a"/>
          <stop offset="0.8" stop-color="#1d6f99"/>
          <stop offset="1" stop-color="#00a3e4"/>
        </linearGradient>
        <clipPath id="portraitClip">
          <path d="M240 60 H545 V330 A165 165 0 0 1 300 450 H240 Z"/>
        </clipPath>
      </defs>
      <path class="band-grey" fill="var(--band-grey)" d="M60 0 H365 L505 66 Q575 100 575 160 Q575 225 520 240 L300 115 Z"/>
      <path class="band-grey-deep" fill="var(--band-grey-deep)" d="M150 0 H245 L330 40 L320 80 Z"/>
      <path class="shape-blue" fill="var(--brand-blue)" d="M0 0 H65 L330 128 L391 150 V480 L0 345 Z"/>
      <path fill="var(--brand-blue-deep)" d="M65 0 H150 L320 80 L330 128 Z" opacity="0.6"/>
      <circle class="shape-blue" fill="var(--brand-blue)" cx="391" cy="315" r="165"/>
      <g role="img" aria-label="Portrait photo of Rudy Fenwick, smiling, arms crossed, black T-shirt" clip-path="url(#portraitClip)">
        <rect x="235" y="35" width="310" height="420" rx="60" fill="url(#portraitTone)"/>
      </g>
      <circle class="name-disc" fill="var(--disc-grey)" cx="369" cy="505" r="61"/>
      <g stroke="var(--rule)" stroke-width="1">
        <line x1="23" y1="587" x2="573" y2="587"/>
        <line x1="23" y1="620" x2="573" y2="620"/>
        <line x1="23" y1="653" x2="573" y2="653"/>
        <line x1="23" y1="686" x2="573" y2="686"/>
        <line x1="23" y1="719" x2="573" y2="719"/>
        <line x1="23" y1="753" x2="573" y2="753"/>
        <line x1="23" y1="786" x2="573" y2="786"/>
        <line x1="23" y1="819" x2="573" y2="819"/>
      </g>
    </svg>

    <h1 class="headline">
      <span class="headline__lead">SMS Me</span>
      <span class="headline__line">For a free</span>
      <span class="headline__line">Personalised</span>
      <span class="headline__line">Health</span>
      <span class="headline__line">Consultation</span>
    </h1>

    <ul class="contact-list">
      <li><span class="icon"><svg viewBox="0 0 10 10"><path d="M2 0.5 L3.6 0.5 L4.2 2.8 L3.1 3.6 Q4 5.8 6.4 6.9 L7.2 5.8 L9.5 6.4 V8 Q9.5 9.5 8 9.5 Q1 8.8 0.5 2 Q0.5 0.5 2 0.5Z"/></svg></span>AUSTRALIA: +61 400 000 000</li>
      <li><span class="icon"></span>SINGAPORE: +65 9000 0000</li>
      <li><span class="icon"><svg viewBox="0 0 10 10"><path d="M0 1.5 H10 V8.5 H0Z M0.8 2.2 L5 5.5 L9.2 2.2" fill="none" stroke="var(--ink-soft)" stroke-width="1.2"/></svg></span>RUDY@RUDYFENWICK.EXAMPLE</li>
      <li><span class="icon"><svg viewBox="0 0 10 10"><circle cx="5" cy="5" r="4.5"/><path d="M2.5 3 Q4 2.5 4.5 4 Q3.5 5.5 5 6.5 L4.5 8.5 M6.5 1.5 Q6 3 7.5 3.5 L8.8 4" fill="none" stroke="#fff" stroke-width="0.9"/></svg></span>WWW.RUDYFENWICK.EXAMPLE</li>
    </ul>

    <div class="signature signature--front">Rudy&nbsp; Fenwick</div>
    <div class="signature signature--faint" aria-hidden="true">Rudy&nbsp; Fenwick</div>
  </section>

  <!-- Back page -->
  <section class="page page--back">
    <svg class="page__art" viewBox="0 0 596 842" preserveAspectRatio="none">
      <defs>
        <linearGradient id="portraitGrey" x1="0" y1="0" x2="0" y2="1">
          <stop offset="0" stop-color="#d0d0d0"/>
          <stop offset="0.5" stop-color="#6b6b6b"/>
          <stop offset="1" stop-color="#3a3a3a"/>
        </linearGradient>
      </defs>
      <circle fill="#f1f1f3" cx="513" cy="812" r="102"/>
      <g stroke="var(--rule)" stroke-width="1">
        <line x1="23" y1="40" x2="573" y2="40"/>
        <line x1="23" y1="73" x2="573" y2="73"/>
        <line x1="23" y1="106" x2="573" y2="106"/>
        <line x1="23" y1="140" x2="573" y2="140"/>
        <line x1="23" y1="173" x2="573" y2="173"/>
        <line x1="23" y1="206" x2="573" y2="206"/>
        <line x1="23" y1="240" x2="573" y2="240"/>
        <line x1="23" y1="273" x2="573" y2="273"/>
        <line x1="23" y1="306" x2="573" y2="306"/>
        <line x1="23" y1="339" x2="573" y2="339"/>
        <line x1="23" y1="373" x2="573" y2="373"/>
        <line x1="23" y1="406" x2="573" y2="406"/>
        <line x1="23" y1="439" x2="573" y2="439"/>
        <line x1="23" y1="473" x2="573" y2="473"/>
        <line x1="23" y1="506" x2="573" y2="506"/>
        <line x1="23" y1="539" x2="573" y2="539"/>
        <line x1="23" y1="572" x2="573" y2="572"/>
        <line x1="103" y1="605" x2="573" y2="605"/>
        <line x1="103" y1="638" x2="573" y2="638"/>
        <line x1="128" y1="672" x2="573" y2="672"/>
        <line x1="153" y1="705" x2="573" y2="705"/>
        <line x1="163" y1="738" x2="573" y2="738"/>
      </g>
      <g role="img" aria-label="Greyscale portrait photo of Rudy Fenwick in a black T-shirt">
        <path d="M25 590 Q60 575 95 595 L125 670 L160 765 H0 V690 Q10 660 25 650 Z" fill="url(#portraitGrey)"/>
      </g>
      <path class="footer-band" fill="var(--footer-black)" d="M0 765 H433 L418 822 H0 Z"/>
      <path class="footer-blue" fill="var(--brand-blue)" d="M423 805 H596 V842 H0 V822 H418 Z"/>
      <line x1="208" y1="775" x2="208" y2="812" stroke="#fff" stroke-width="0.8"/>
      <line x1="452" y1="800" x2="596" y2="800" stroke="#3a3a8a" stroke-width="0.8"/>
    </svg>

    <div class="footer-contacts">
      <ul class="footer-contacts__col footer-contacts__col--phone">
        <li><span class="icon"><svg viewBox="0 0 10 10"><path d="M2 0.5 L3.6 0.5 L4.2 2.8 L3.1 3.6 Q4 5.8 6.4 6.9 L7.2 5.8 L9.5 6.4 V8 Q9.5 9.5 8 9.5 Q1 8.8 0.5 2 Q0.5 0.5 2 0.5Z"/></svg></span>AUSTRALIA:<span class="gap"></span>+61 400 000 000</li>
        <li><span class="icon"></span>SINGAPORE: +65 9000 0000</li>
      </ul>
      <ul class="footer-contacts__col footer-contacts__col--web">
        <li><span class="icon"><svg viewBox="0 0 10 10"><path d="M0 1.5 H10 V8.5 H0Z"/><path d="M0.8 2.2 L5 5.5 L9.2 2.2" fill="none" stroke="#0c0c0c" stroke-width="1"/></svg></span>RUDY@RUDYFENWICK.EXAMPLE</li>
        <li><span class="icon"><svg viewBox="0 0 10 10"><circle cx="5" cy="5" r="4.5"/><path d="M2.5 3 Q4 2.5 4.5 4 Q3.5 5.5 5 6.5 L4.5 8.5 M6.5 1.5 Q6 3 7.5 3.5 L8.8 4" fill="none" stroke="#0c0c0c" stroke-width="0.9"/></svg></span>WWW.RUDYFENWICK.EXAMPLE</li>
      </ul>
    </div>

    <div class="signature signature--back">Rudy&nbsp; Fenwick</div>
  </section>

</div>
</body>
</html>
```